Fernvale Pharmacy opening

We want to have a double sided 5.5"x8.5" flyer for a new Pharmacy opening in a well known strip mall in the neighborhood and we are planning to mail it to neighbors homes.

Want to put the outside pharmacy picture on the main side of the flyer and a coupon with 25% off towards an OTC product on the back in addition to the info below (preferably in a sort of bulletin points not a list (something like the 2 examples attached).

Colors to be red like the exterior sign and blue like the interior wall paint:

Front side should have:
Fernvale pharmacy
Your locally owned and operated pharmacy around the corner.
317-4082 Tarrow rd.
Brisket hollow plaza
T. 604 827 5530 (call or text)
F. 604-827-5532

Free prescription delivery
Text us for refills
Specialized compounding
Customized compression stockings

The back side should have:

Do you forget taking your medications! We offer multiple compliance packaging options at no additional cost.
Had shingles before or worried to have it? travelling soon? check our vaccinations options!
Suffering side effects? We are experienced to check your medications interactions & different coverage options.
Hard time monitoring your blood pressure? Trying to stop smoking? we can always help.

FEELING BETTER STARTS HERE

```html
<!DOCTYPE html>
<html lang="en">
<head>
<meta charset="utf-8">
<title>Fernvale Pharmacy – Opening Flyer</title>
<link rel="stylesheet" href="https://fonts.googleapis.com/css2?family=Arimo:wght@700&family=Fira+Sans:wght@600;700;800&family=Oswald:wght@500;600&family=Source+Sans+3:wght@400;600;700&display=swap">
<style>
  :root {
    --red: #ee1c1c;
    --red-deep: #d90f12;
    --ink: #1f1f1f;
    --charcoal: #333436;
    --white: #ffffff;
    --backdrop: #e4e4e4;
    --mint: #e3f0dd;
    --wall-blue: #3f5a95;
  }
  * { box-sizing: border-box; margin: 0; padding: 0; }
  html, body { width: 1200px; height: 904px; overflow: hidden; }
  body { background: var(--backdrop); position: relative; font-family: "Source Sans 3", sans-serif; }

  .flyer {
    position: absolute; top: 96px; width: 460px; height: 712px;
    background: var(--white); overflow: hidden;
    box-shadow: 0 2px 8px rgba(0,0,0,.12);
  }
  .flyer--front { left: 110px; }
  .flyer--back { left: 630px; background: linear-gradient(180deg, #f4f4f2 0%, #f0f4ec 55%, var(--mint) 100%); }

  .brand { position: absolute; left: 20px; top: 16px; z-index: 3; display: flex; align-items: center; gap: 10px; }
  .brand__name { font-family: "Arimo", sans-serif; font-weight: 700; color: var(--red); font-size: 22px; line-height: 22px; letter-spacing: .3px; }
  .brand__dot { width: 48px; height: 48px; border-radius: 50%; background: var(--red); }

  .photo { position: absolute; left: 0; }
  .photo--storefront { top: 74px; width: 460px; height: 296px;
    background: linear-gradient(180deg, #6e6a66 0%, #8d857c 30%, #9aa0a6 60%, #c9cbcd 85%, rgba(255,255,255,0) 100%); }
  .photo--interior { top: 0; width: 460px; height: 400px;
    background: linear-gradient(180deg, #f2f2f0 0%, #f2f2f0 22%, var(--wall-blue) 30%, #566fa3 42%, #e8dcc6 55%, #e8e4dc 80%, rgba(240,244,236,0) 100%); }

  .tagline { position: absolute; left: 21px; top: 372px; width: 200px; font-family: "Oswald", sans-serif; font-weight: 500; font-size: 20px; line-height: 27px; color: var(--ink); white-space: nowrap; }
  .tagline span { display: block; }
  .tagline__accent { color: var(--red); font-weight: 600; text-transform: uppercase; }
  .tagline__tail { color: var(--red); }

  .art--mascots { position: absolute; left: 16px; top: 478px; width: 200px; height: 190px; border-radius: 10px;
    background: radial-gradient(ellipse at 50% 45%, #f3f3f3 0%, #e9e9ea 60%, #ffffff 100%); }

  .services { position: absolute; left: 229px; top: 350px; width: 209px; height: 320px;
    background: var(--red); border-radius: 0 0 10px 10px; list-style: none; padding-top: 22px; }
  .service { display: flex; align-items: center; height: 69px; padding-left: 13px; }
  .service__icon { width: 58px; height: 58px; border-radius: 50%; background: var(--white); flex: none; display: flex; align-items: center; justify-content: center; }
  .service__label { margin-left: 15px; font-family: "Fira Sans", sans-serif; font-weight: 600; color: var(--white); font-size: 15px; line-height: 19px; }
  .service__label--caps { text-transform: uppercase; font-weight: 700; }

  .headline { position: absolute; left: 20px; top: 350px; font-family: "Fira Sans", sans-serif; }
  .headline__lead { font-weight: 700; font-size: 22px; color: var(--ink); display: block; line-height: 27px; }
  .headline__main { font-weight: 800; font-size: 23px; color: var(--red); display: block; line-height: 28px; text-transform: uppercase; }

  .pitch { position: absolute; left: 20px; top: 420px; width: 240px; font-size: 11.2px; line-height: 14px; color: var(--ink); }
  .pitch strong { font-weight: 700; }
  .pitch .hl { color: var(--red); font-weight: 700; }
  .pitch .gap { margin-top: 10px; }
  .pitch .cta { color: var(--red); font-family: "Fira Sans", sans-serif; font-weight: 700; font-size: 13px; margin-top: 6px; text-transform: uppercase; }

  .slogan { position: absolute; left: 20px; top: 612px; font-family: "Fira Sans", sans-serif; font-weight: 700; font-size: 16px; line-height: 20px; text-transform: uppercase; }
  .slogan span { display: block; }
  .slogan__top { color: var(--ink); }
  .slogan__bottom { color: var(--red); }

  .art--capsule { position: absolute; left: 262px; top: 395px; width: 180px; height: 185px; border-radius: 12px;
    background: radial-gradient(ellipse at 55% 55%, #a8d98a 0%, #cfe8c0 45%, rgba(227,240,221,0) 80%); }

  .coupon { position: absolute; left: 262px; top: 590px; width: 180px; height: 76px;
    border: 2px dashed var(--red); border-radius: 8px; background: var(--white);
    display: flex; flex-direction: column; align-items: center; justify-content: center; text-align: center; }
  .coupon__value { font-family: "Fira Sans", sans-serif; font-weight: 800; font-size: 24px; line-height: 26px; color: var(--red); }
  .coupon__terms { font-family: "Fira Sans", sans-serif; font-weight: 600; font-size: 11px; line-height: 14px; color: var(--ink); }

  .footer { position: absolute; left: 0; bottom: 0; width: 460px; height: 40px; }
  .footer__band { position: absolute; left: 0; top: 0; }
  .footer__item { position: absolute; display: flex; align-items: center; gap: 5px; color: var(--white); font-size: 11px; line-height: 13px; font-weight: 600; }
  .footer__item svg { flex: none; }
  .footer__address { left: 20px; top: 6px; }
  .footer__phone { left: 190px; top: 11px; }
  .footer__fax { left: 352px; top: 11px; }
</style>
</head>
<body>

<section class="flyer flyer--front">
  <div class="brand">
    <div class="brand__name">FERNVALE<br>PHARMACY</div>
    <div class="brand__dot"></div>
  </div>

  <div class="photo photo--storefront" role="img" aria-label="Photograph of the pharmacy storefront in the strip mall with its red exterior sign"></div>

  <h1 class="tagline">
    <span class="tagline__accent">Your locally owned</span>
    <span>and operated pharmacy</span>
    <span class="tagline__tail">around the corner.</span>
  </h1>

  <div class="art--mascots" role="img" aria-label="Illustration of cartoon pill and tablet characters"></div>

  <ul class="services">
    <li class="service">
      <span class="service__icon">
        <svg width="34" height="26" viewBox="0 0 34 26" fill="none" stroke="#ee1c1c" stroke-width="2">
          <rect x="1" y="4" width="20" height="14" rx="1"/>
          <path d="M21 8h7l4 5v5H21z"/>
          <circle cx="8" cy="21" r="3"/><circle cx="26" cy="21" r="3"/>
        </svg>
      </span>
      <span class="service__label service__label--caps">Free<br>prescription<br>delivery</span>
    </li>
    <li class="service">
      <span class="service__icon">
        <svg width="32" height="32" viewBox="0 0 32 32" fill="none" stroke="#ee1c1c" stroke-width="2">
          <path d="M5 14a11 11 0 0 1 20-6"/><path d="M25 3v5h-5"/>
          <path d="M27 18a11 11 0 0 1-20 6"/><path d="M7 29v-5h5"/>
          <rect x="11" y="12" width="10" height="8" rx="4"/>
        </svg>
      </span>
      <span class="service__label">Text us<br>for refills</span>
    </li>
    <li class="service">
      <span class="service__icon">
        <svg width="32" height="32" viewBox="0 0 32 32" fill="none" stroke="#ee1c1c" stroke-width="2">
          <path d="M10 4l6 3.5v7L10 18l-6-3.5v-7z"/>
          <path d="M22 14l6 3.5v7L22 28l-6-3.5v-7z"/>
          <path d="M16 11l6 3"/>
        </svg>
      </span>
      <span class="service__label">Specialized<br>compounding</span>
    </li>
    <li class="service">
      <span class="service__icon">
        <svg width="26" height="32" viewBox="0 0 26 32" fill="none" stroke="#ee1c1c" stroke-width="2">
          <path d="M9 2h9v16l5 6v5h-12l-4-6z"/>
        </svg>
      </span>
      <span class="service__label">Customized<br>compression<br>stockings</span>
    </li>
  </ul>

  <footer class="footer">
    <svg class="footer__band" viewBox="0 0 460 40" width="460" height="40">
      <rect width="460" height="40" fill="#333436"/>
      <polygon points="0,0 160,0 178,34 460,34 460,40 0,40" fill="#ee1c1c"/>
    </svg>
    <div class="footer__item footer__address">
      <svg width="12" height="12" viewBox="0 0 12 12" fill="none" stroke="#fff" stroke-width="1.2"><circle cx="6" cy="6" r="5.3"/><path d="M6 9.5S3.6 6.8 3.6 5.2a2.4 2.4 0 0 1 4.8 0C8.4 6.8 6 9.5 6 9.5z"/></svg>
      <span>317-4082 Tarrow rd.<br>Brisket hollow plaza</span>
    </div>
    <div class="footer__item footer__phone">
      <svg width="12" height="12" viewBox="0 0 12 12" fill="none" stroke="#ee1c1c" stroke-width="1.2"><circle cx="6" cy="6" r="5.3"/><path d="M4 3.5l1 1.6-.6.8a4 4 0 0 0 1.7 1.7l.8-.6 1.6 1-.5 1a4.8 4.8 0 0 1-4.9-4.9z"/></svg>
      <span>604 827 5530 (call or text)</span>
    </div>
    <div class="footer__item footer__fax">
      <svg width="12" height="12" viewBox="0 0 12 12" fill="none" stroke="#ee1c1c" stroke-width="1.2"><circle cx="6" cy="6" r="5.3"/><rect x="3.5" y="5" width="5" height="3"/><path d="M4.5 5V3.3h3V5"/></svg>
      <span>604-827-5532</span>
    </div>
  </footer>
</section>

<section class="flyer flyer--back">
  <div class="photo photo--interior" role="img" aria-label="Photograph of the pharmacy interior with blue walls, shelves of products and counter signs for vaccines, prescriptions and compounding"></div>

  <div class="brand">
    <div class="brand__name">FERNVALE<br>PHARMACY</div>
    <div class="brand__dot"></div>
  </div>

  <h2 class="headline">
    <span class="headline__lead">Do you forget taking</span>
    <span class="headline__main">Your medications!</span>
  </h2>

  <div class="pitch">
    <p><span class="hl">WE OFFER</span> multiple compliance packaging options at no additional cost.</p>
    <p><strong>Had shingles before or worried to have it?</strong></p>
    <p>Travelling soon?</p>
    <p>Check our vaccinations options!</p>
    <p class="gap"><span class="hl">Suffering side effects?</span></p>
    <p>We are experienced to check your <strong>medications interactions</strong> &amp; <strong>different coverage</strong> options.</p>
    <p>Hard time monitoring your <strong>blood pressure</strong>?</p>
    <p>Trying to <strong>stop smoking</strong>?</p>
    <p class="cta">We can always help.</p>
  </div>

  <div class="slogan">
    <span class="slogan__top">Feeling better</span>
    <span class="slogan__bottom">Starts here</span>
  </div>

  <div class="art--capsule" role="img" aria-label="Illustration of an open green capsule with a leafy plant and health icons growing out of it"></div>

  <div class="coupon">
    <span class="coupon__value">25% OFF</span>
    <span class="coupon__terms">any one OTC product<br>with this coupon</span>
  </div>

  <footer class="footer">
    <svg class="footer__band" viewBox="0 0 460 40" width="460" height="40">
      <rect width="460" height="40" fill="#333436"/>
      <polygon points="0,0 160,0 178,34 460,34 460,40 0,40" fill="#ee1c1c"/>
    </svg>
    <div class="footer__item footer__address">
      <svg width="12" height="12" viewBox="0 0 12 12" fill="none" stroke="#fff" stroke-width="1.2"><circle cx="6" cy="6" r="5.3"/><path d="M6 9.5S3.6 6.8 3.6 5.2a2.4 2.4 0 0 1 4.8 0C8.4 6.8 6 9.5 6 9.5z"/></svg>
      <span>317-4082 Tarrow rd.<br>Brisket hollow plaza</span>
    </div>
    <div class="footer__item footer__phone">
      <svg width="12" height="12" viewBox="0 0 12 12" fill="none" stroke="#ee1c1c" stroke-width="1.2"><circle cx="6" cy="6" r="5.3"/><path d="M4 3.5l1 1.6-.6.8a4 4 0 0 0 1.7 1.7l.8-.6 1.6 1-.5 1a4.8 4.8 0 0 1-4.9-4.9z"/></svg>
      <span>604 827 5530 (call or text)</span>
    </div>
    <div class="footer__item footer__fax">
      <svg width="12" height="12" viewBox="0 0 12 12" fill="none" stroke="#ee1c1c" stroke-width="1.2"><circle cx="6" cy="6" r="5.3"/><rect x="3.5" y="5" width="5" height="3"/><path d="M4.5 5V3.3h3V5"/></svg>
      <span>604-827-5532</span>
    </div>
  </footer>
</section>

</body>
</html>
```